Willowmere Wellness Academy (Massage School) Flyer Advertisment

We are a massage therapy/holistic healing school, operating in Los Angeles for over 16 years. We need a flyer/advertisement with the aim of attracting new students and potential future massage therapists. Our vision is a 4x6 (read vertical) flyer (potentially dual sided, due to amount of copy we have). The key aesthetic terms for this project are modern, feminine, minimal, natural, fun. The design should be eye catching yet feel organic (we want an advertisement, but keep in mind we are a holistic health institution.) We would like the primary color scheme to be focused around purple and white (green or beige are secondary), and would very much like to see the use of a literal Lavender plant (or multiple) included creatively. You do not need to use all the files we provided. Mandatory is the inclusion of ALL the copy provided in the word document attached, arranged at your discretion, as well as the logo file. We have also provided a picture of our school as well as a few massage photos to possibly be used (only if applicable). Please feel free to be creative with the exact font choices and exact color choices (we only selected the options here as reference.) Thank you all so much for your time and we look forward to reviewing the designs. *Note* we have selected a 5 day duration due to urgency but may be willing to extend for the right designer (please reach out to us if need be)

Target Market(s)

Potential students to become massage therapists or holistic health professionals

Industry/Entity Type

Education

Font styles to use
Sans Serif
Script

Colors
6b449b
ffffff
fbc994
9bcb3c

Requirements
Must have
• Use of Copy attached. Use of logo. use of Lavender plant
Nice to have
• Photo our school (included). Photos of massages being done on clients (examples included)
• * Would be great if you could allow room for rounded corners on the print job* not necessary

```html
<!DOCTYPE html>
<html lang="en">
<head>
<meta charset="utf-8">
<title>Willowmere Wellness Academy – Flyer</title>
<link href="https://fonts.googleapis.com/css2?family=Lobster&family=Montserrat:wght@400;500;600&display=swap" rel="stylesheet">
<style>
  :root{
    --bg:#000;
    --purple:#5e2f8e;
    --purple-dark:#4b2176;
    --purple-soft:#9a86c6;
    --lavender-bg:#e7e2f0;
    --white:#fff;
    --grey:#7a7a80;
    --ink:#2e2e33;
    --skin:#e2b898;
    --sky:#c9d8e6;
  }
  *{margin:0;padding:0;box-sizing:border-box}
  html,body{width:1200px;height:918px;overflow:hidden;background:var(--bg)}
  body{position:relative;font-family:"Montserrat",Arial,sans-serif}
  .panel{position:absolute;top:35px;width:564px;height:847px;overflow:hidden}
  .panel--front{left:32px;background:var(--purple)}
  .panel--back{left:604px;background:var(--lavender-bg)}
  .panel svg.art{position:absolute;left:0;top:0}
  .badge{position:absolute;border-radius:50%;background:var(--white);border:3px solid var(--purple);
    display:flex;align-items:center;justify-content:center;text-align:center;
    color:var(--purple);font-weight:600;line-height:1.15}
  .badge--front{left:390px;top:347px;width:144px;height:144px;font-size:15px}
  .badge--back{left:400px;top:309px;width:124px;height:124px;font-size:13px}
  .headline{position:absolute;left:48px;top:428px;font-family:"Lobster",cursive;font-weight:400;
    color:var(--white);font-size:40px;line-height:48px}
  .course-list{position:absolute;left:48px;top:544px;width:440px;color:var(--white);
    font-size:15.5px;line-height:19.6px}
  .thumb{position:absolute;top:666px;width:199px;height:114px}
  .thumb--massage{left:42px}
  .thumb--oils{left:261px}
  .site-link{position:absolute;left:42px;top:801px;color:var(--white);font-size:14px;font-weight:500}
  .intro{position:absolute;left:36px;top:417px;color:var(--purple);font-size:19px;font-weight:600;line-height:25px}
  .benefits{position:absolute;left:36px;top:508px;width:328px;list-style:none}
  .benefits li{position:relative;padding:0 0 4px 16px;margin-bottom:7px;color:var(--ink);
    font-size:15px;line-height:18.5px;border-bottom:1px solid var(--purple-soft)}
  .benefits li:last-child{border-bottom:none}
  .benefits li::before{content:"";position:absolute;left:2px;top:7px;width:5px;height:5px;border-radius:50%;background:var(--purple)}
  .benefits strong{font-weight:600}
  .licensing{position:absolute;left:36px;top:697px;width:345px;color:var(--grey);font-size:11.4px;line-height:15.5px}
  .contact{position:absolute;left:36px;top:764px;color:var(--ink);font-size:14.5px;line-height:19.5px}
  .contact .name{font-size:16px;font-weight:600;margin-bottom:2px}
  .contact .site{font-weight:600}
  .cta{position:absolute;left:378px;width:163px;background:var(--purple);color:var(--white);
    border:1px solid var(--purple-soft);border-radius:4px;text-align:center;font-size:13.5px;line-height:18px;padding:2px 4px}
  .cta--open{top:476px;height:41px}
  .cta--reviews{top:535px;height:42px}
  .footer-bar{position:absolute;left:0;bottom:0;width:100%;height:10px;background:var(--purple)}
</style>
</head>
<body>

<section class="panel panel--front">
  <svg class="art" width="564" height="847" viewBox="0 0 564 847">
    <defs>
      <linearGradient id="spa-photo" x1="0" y1="0" x2="1" y2="1">
        <stop offset="0" stop-color="#f6f3f2"/>
        <stop offset="0.5" stop-color="var(--skin)"/>
        <stop offset="1" stop-color="#f1ece9"/>
      </linearGradient>
      <radialGradient id="lavender" cx="0.5" cy="0.5" r="0.5">
        <stop offset="0" stop-color="#7b52b8"/>
        <stop offset="0.7" stop-color="#6a44a3" stop-opacity="0.8"/>
        <stop offset="1" stop-color="#5e2f8e" stop-opacity="0"/>
      </radialGradient>
    </defs>
    <rect class="hero-photo" width="564" height="440" fill="url(#spa-photo)" role="img" aria-label="Photo of a therapist giving a back massage to a client lying on a white towel"/>
    <polygon points="0,350 564,420 564,440 0,372" fill="var(--purple-soft)"/>
    <polygon points="0,372 564,440 564,847 0,847" fill="var(--purple)"/>
    <rect x="360" y="513" width="192" height="334" rx="40" fill="url(#lavender)" role="img" aria-label="Sprigs of purple lavender flowers"/>
  </svg>
  <div class="badge badge--front">Willowmere<br>Wellness<br>Academy</div>
  <h1 class="headline">Become a Certified<br>Massage Therapist!</h1>
  <p class="course-list">WWA offers courses in Swedish, Deep Tissue, Myofascial Releaase, Chair Massage, Aromatherapy, Energy Healing, Crystal &amp; Gemstone Therapy, Shiatsu, Lymphatic, Sports Massage, Pregnancy Massage,Hot Stone Massage, Polarity Therapy and more!</p>
  <svg class="thumb thumb--massage" viewBox="0 0 199 114">
    <polygon points="14,1 198,1 198,113 14,113 1,100 1,14" fill="none" stroke="var(--purple-soft)" stroke-width="1.5"/>
    <polygon points="18,7 192,7 192,107 26,107 8,92 8,18" fill="#d9b59b" role="img" aria-label="Close-up photo of hands massaging a client's back"/>
  </svg>
  <svg class="thumb thumb--oils" viewBox="0 0 197 114">
    <polygon points="1,1 183,1 196,14 196,100 183,113 1,113" fill="none" stroke="var(--purple-soft)" stroke-width="1.5"/>
    <polygon points="7,7 178,7 189,18 189,96 178,107 7,107" fill="#6d4a3a" role="img" aria-label="Photo of amber essential oil bottles among lavender"/>
  </svg>
  <p class="site-link">www.willowmerewellness.org</p>
</section>

<section class="panel panel--back">
  <svg class="art" width="564" height="847" viewBox="0 0 564 847">
    <defs>
      <linearGradient id="school-photo" x1="0" y1="0" x2="0" y2="1">
        <stop offset="0" stop-color="var(--sky)"/>
        <stop offset="0.55" stop-color="#6b6358"/>
        <stop offset="1" stop-color="#4c5a3c"/>
      </linearGradient>
      <radialGradient id="lavender-back" cx="0.5" cy="0.5" r="0.5">
        <stop offset="0" stop-color="#7b52b8"/>
        <stop offset="0.7" stop-color="#6a44a3" stop-opacity="0.75"/>
        <stop offset="1" stop-color="#7b52b8" stop-opacity="0"/>
      </radialGradient>
    </defs>
    <rect width="564" height="420" fill="url(#school-photo)" role="img" aria-label="Photo of the academy's round glass office building with trees"/>
    <polygon points="0,402 564,328 564,352 0,420" fill="var(--purple)"/>
    <polygon points="0,420 564,352 564,847 0,847" fill="var(--lavender-bg)"/>
    <rect x="376" y="601" width="172" height="236" rx="40" fill="url(#lavender-back)" role="img" aria-label="Sprigs of purple lavender flowers"/>
  </svg>
  <div class="badge badge--back">Willowmere<br>Wellness<br>Academy</div>
  <h2 class="intro">WWA has been educating students<br>from around the world and<br>all walks of life for over 16 years!</h2>
  <ul class="benefits">
    <li>Complete an affordable <strong>300 CEU Hour</strong> Program in 15 Weeks</li>
    <li>2500+ Hours of Advanced Electives in various modalities</li>
    <li>Many classes open to the public and non-body-workers</li>
    <li>Study with accomplished holistic healers and seasoned health professionals</li>
  </ul>
  <p class="licensing">WWA is licensed to operate by the Office of Private Vocational Education and fully approved by the Regional Massage Therapy Council as well as the State Board of Nursing.</p>
  <address class="contact" style="font-style:normal">
    <p class="name">Willowmere Wellness Academy</p>
    <p>1420 Larkspur Ave., Los Angeles, CA 90041</p>
    <p>(818) 555-0147 &nbsp;<span class="site">www.willowmerewellness.org</span></p>
  </address>
  <p class="cta cta--open">*Ask us about our next Open House*</p>
  <p class="cta cta--reviews">*Check out our reviews on Reviewly*</p>
  <div class="footer-bar"></div>
</section>

</body>
</html>
```